FRESH WEB DESIGN FOR A HEALTH - SOCIAL NETWORK

We are currently looking for a creative, fresh, vibrant, inspiring design for a new social network focused on health and nutrition for health professionals (namely nutritionists) and end-users.

Design requirements - IMPORTANT: please see attached file 'LumaGrove web site design scope' for the detailed brief.

The web site requires new design templates with inter-changeable banners and in some cases profile images. It's important for the website to communicate LumaGrove's core values and image which includes fun, vitality, freshness, life fulfillment, trust, integrity and loyalty to the two target groups. Imagery must have a consistent/inter-related theme across all communities, topics and resources, which need to be easily applied to the web site.To help engage our audience we are looking for something fresh and unique in the selected imagery/ theme/ design templates.

The chosen design will need to be applied to create a PDF, PowerPoint and business card template.

Please see attached file 'LumaGrove web site design scope' to view the LumaGrove web site, which is currently under development.

Industry/Entity Type

Nutrition

```html
<!DOCTYPE html>
<html lang="en">
<head>
<meta charset="utf-8">
<title>LumaGrove – Health Network</title>
<link href="https://fonts.googleapis.com/css2?family=Roboto:wght@300;400;500;700&family=Roboto+Condensed:wght@700&display=swap" rel="stylesheet">
<style>
:root{
  --blue:#1a8fd6;
  --green:#5ab031;
  --green-2:#36a04a;
  --orange:#f39a1c;
  --ink:#333;
  --line:#d9d9d9;
  --fb:#3b5998;
}
*{box-sizing:border-box;margin:0;padding:0}
html,body{width:782px;height:1200px;overflow:hidden;background:#fff}
body{font-family:'Roboto',Arial,sans-serif;color:var(--ink);position:relative}
.page{position:absolute;left:94px;top:0;width:594px;height:1200px;background:#fff;box-shadow:0 0 4px rgba(0,0,0,.12)}
.abs{position:absolute}
/* header */
.brand{left:10px;top:18px;display:flex;align-items:center;gap:6px}
.brand-dot{width:22px;height:22px;border-radius:50%;background:var(--green)}
.brand-name{font-size:22px;font-weight:500;color:var(--green);letter-spacing:.2px}
.nav{right:12px;top:21px;display:flex;font-size:8.4px;text-transform:uppercase}
.nav a{color:#222;text-decoration:none;padding:0 11px;border-left:1px solid var(--line);line-height:20px}
.nav a:first-child{border-left:0}
/* hero */
.hero{left:6px;top:62px;width:582px;height:300px;background:linear-gradient(180deg,#1c86c8 0%,#3ea4dd 70%,#6bbbe6 100%)}
.hero-title{left:338px;top:56px;font-size:19px;font-weight:300;color:#fff;line-height:25px}
.hero-play{left:258px;top:120px}
.hero-prev{left:22px;top:134px}
.hero-next{left:540px;top:134px}
/* features */
.feature{top:376px;width:124px;font-size:8px;line-height:12px;color:#333}
.feature .ico{height:28px;display:block}
.feature h3{font-size:9.6px;font-weight:500;margin:7px 0 0;line-height:12px}
.feature ul{list-style:none}
.sep{top:378px;width:1px;height:188px;background:var(--line)}
.nutrition h3{color:var(--green)}
.energy h3{color:var(--orange)}
.wellness h3{color:var(--green-2)}
.exercise h3{color:var(--ink)}
.rule{left:8px;top:582px;width:578px;height:1px;background:var(--line)}
/* discussions */
.section-title{font-size:9.6px;font-weight:500;color:var(--blue);text-transform:uppercase}
.card{width:175px}
.card .img{height:129px;position:relative}
.card .label{position:absolute;left:0;right:0;bottom:0;height:26px;background:rgba(30,30,30,.82);color:#fff;font-family:'Roboto Condensed',Arial,sans-serif;font-size:8px;font-weight:700;text-transform:uppercase;display:flex;align-items:center;justify-content:center}
.card p{font-size:7.5px;line-height:10px;color:#333;margin-top:6px}
/* networks */
.networks-sub{font-size:7.6px;color:#333}
.net-list{list-style:none;width:88px;font-size:7.6px}
.net-list li{height:21px;display:flex;align-items:center;gap:7px;border-bottom:1px solid var(--line)}
.net-list li:last-child{border-bottom:0}
.net-ico{width:9px;height:9px;border-radius:50%;background:#555;flex:none}
/* activity */
.activity{top:839px;width:208px;height:139px;border:1px solid #c5cbd8;background:#f6f7f9}
.activity-head{height:20px;background:#3f5b9b;color:#fff;font-size:7.6px;display:flex;align-items:center;justify-content:space-between;padding:0 8px}
.activity-head span.sq{width:8px;height:8px;background:#6d86bd}
.act{display:flex;gap:6px;padding:6px 8px 0 9px;font-size:6.2px;line-height:8px;color:#555}
.act .ava{width:19px;height:19px;background:#9aa0a8;flex:none}
.act b{color:var(--fb);font-weight:500}
.act i{font-style:normal;color:#999}
.act .ln{color:var(--fb)}
/* signup */
.signup{left:0;top:987px;width:594px;height:151px;background:linear-gradient(90deg,#5c5c5c,#4a4a4a 50%,#6a5a44)}
.signup-btn{left:232px;top:19px;width:129px;height:29px;border:1.5px solid #fff;color:#fff;font-size:9.6px;display:flex;align-items:center;justify-content:center}
.signup-text{left:0;top:60px;width:594px;text-align:center;color:#fff;font-size:8px;line-height:14px}
.field{top:102px;height:28px;background:#fff;border:1px solid #aaa;font-size:8px;color:#444;padding-left:8px;display:flex;align-items:center}
.go{left:423px;top:102px;width:76px;height:28px;background:var(--blue);color:#fff;font-size:9.6px;font-weight:500;display:flex;align-items:center;justify-content:center}
/* footer */
.footer{left:0;top:1138px;width:594px;height:62px;background:var(--blue)}
.footer,.footer a{color:#fff;font-size:6.6px;font-weight:500;text-transform:uppercase;text-decoration:none}
.follow{left:6px;top:20px}
.socials{left:8px;top:30px;display:flex;gap:2px}
.socials span{width:15px;height:15px;background:#1f5da8;border:1px solid #fff}
.foot-nav{right:7px;top:20px}
.foot-nav a{padding:0 4px}
.copy{right:7px;top:35px}
</style>
</head>
<body>
<div class="page">
  <header>
    <div class="abs brand"><span class="brand-dot"></span><span class="brand-name">LumaGrove</span></div>
    <nav class="abs nav"><a>Home</a><a>About Us</a><a>Our Services</a><a>News</a><a>Blog</a><a>Contact Us</a></nav>
  </header>

  <section class="abs hero" role="img" aria-label="Photo of a joyful woman in a blue dress jumping against a bright blue sky">
    <div class="abs hero-title">Share your story and<br>support others</div>
    <svg class="abs hero-play" width="56" height="56" viewBox="0 0 56 56"><circle cx="28" cy="28" r="25" fill="none" stroke="#fff" stroke-width="4"/><path d="M22 17 L40 28 L22 39Z" fill="#fff"/></svg>
    <svg class="abs hero-prev" width="20" height="36" viewBox="0 0 20 36"><path d="M17 2 L3 18 L17 34" fill="none" stroke="#fff" stroke-width="2.5"/></svg>
    <svg class="abs hero-next" width="20" height="36" viewBox="0 0 20 36"><path d="M3 2 L17 18 L3 34" fill="none" stroke="#fff" stroke-width="2.5"/></svg>
  </section>

  <section class="features">
    <div class="abs feature nutrition" style="left:12px">
      <svg class="ico" width="32" height="28" viewBox="0 0 32 28"><path d="M18 12 C18 4 24 2 30 2 C30 8 26 12 18 12Z" fill="#5ab031"/><path d="M17 12 C12 12 10 8 11 5 C15 5 17 8 17 12Z" fill="#5ab031"/><path d="M2 18 H10 L16 16 H24 L30 14 V20 L22 26 H8 L2 24Z" fill="#333"/></svg>
      <h3>NUTRITION</h3>
      <ul><li>Maintaining Health (Knowledge)</li><li>Starting a Healthy Life (No knowledge)</li><li>Health Problem (Disease/ Allergy)</li><li>Lacking Energy</li><li>Weight Problem</li><li>Pregnancy</li><li>Stressed &amp; Fatigued</li><li>Women's Health</li><li>Men's Health</li><li>Children's Health</li><li>50 years +</li></ul>
    </div>
    <div class="abs sep" style="left:147px"></div>
    <div class="abs feature energy" style="left:162px">
      <svg class="ico" width="32" height="28" viewBox="0 0 32 28"><circle cx="16" cy="7" r="4" fill="#f39a1c"/><path d="M3 4 L7 3 L11 12 H21 L25 3 L29 4 L24 16 V26 H8 V16Z" fill="#f39a1c"/></svg>
      <h3>ENERGY</h3>
      <ul><li>Maintaining Health (Knowledge)</li><li>Starting a Healthy Life (No knowledge)</li><li>Health Problem (Disease/ Allergy)</li><li>Lacking Energy</li><li>Weight Problem</li><li>Pregnancy</li><li>Stressed &amp; Fatigued</li><li>Women's Health</li><li>Men's Health</li><li>Children's Health</li><li>50 years +</li></ul>
    </div>
    <div class="abs sep" style="left:298px"></div>
    <div class="abs feature wellness" style="left:313px">
      <svg class="ico" width="32" height="28" viewBox="0 0 32 28"><rect x="2" y="6" width="23" height="20" rx="2" fill="#36a04a"/><rect x="9" y="2" width="9" height="6" fill="none" stroke="#36a04a" stroke-width="2"/><path d="M11.5 10 H15.5 V14 H19.5 V18 H15.5 V22 H11.5 V18 H7.5 V14 H11.5Z" fill="#fff"/></svg>
      <h3>WELLNESS</h3>
      <ul><li>Maintaining Health (Knowledge)</li><li>Starting a Healthy Life (No knowledge)</li><li>Health Problem (Disease/ Allergy)</li><li>Lacking Energy</li><li>Weight Problem</li><li>Pregnancy</li><li>Stressed &amp; Fatigued</li><li>Women's Health</li><li>Men's Health</li><li>Children's Health</li><li>50 years +</li></ul>
    </div>
    <div class="abs sep" style="left:448px"></div>
    <div class="abs feature exercise" style="left:462px">
      <svg class="ico" width="32" height="28" viewBox="0 0 32 28"><circle cx="5" cy="5" r="3.5" fill="#333"/><circle cx="27" cy="5" r="3.5" fill="#333"/><circle cx="16" cy="6" r="4" fill="#333"/><path d="M2 10 H10 L12 14 H20 L22 10 H30 V16 H24 V26 H8 V16 H2Z" fill="#333"/></svg>
      <h3>EXERCISE</h3>
      <ul><li>Maintaining Health (Knowledge)</li><li>Starting a Healthy Life (No knowledge)</li><li>Health Problem (Disease/ Allergy)</li><li>Lacking Energy</li><li>Weight Problem</li><li>Pregnancy</li><li>Stressed &amp; Fatigued</li><li>Women's Health</li><li>Men's Health</li><li>Children's Health</li><li>50 years +</li></ul>
    </div>
  </section>
  <div class="abs rule"></div>

  <section class="discussions">
    <h2 class="abs section-title" style="left:9px;top:595px">Join Discussions &nbsp;- &nbsp;Find Answers</h2>
    <article class="abs card" style="left:10px;top:616px">
      <div class="img" role="img" aria-label="Photo of an optician examining a patient" style="background:linear-gradient(135deg,#d9c9bf,#b88a70)"><div class="label">Achieving Optimal Health</div></div>
      <p>Understanding optimal health; learn about nutrition, cleansing and exercise, and the enormous benefits they bring.</p>
    </article>
    <article class="abs card" style="left:192px;top:616px">
      <div class="img" role="img" aria-label="Photo of a tired doctor resting her head against a window" style="background:linear-gradient(135deg,#6d7a5e,#c9cfc8)"><div class="label">Overcoming Health Problems</div></div>
      <p>Learn how to treat and prevent health problems naturally; diseases such as Alzheimer's and diabetes.</p>
    </article>
    <article class="abs card" style="left:12px;top:792px">
      <div class="img" role="img" aria-label="Photo of a waist wrapped in a measuring tape" style="background:linear-gradient(135deg,#4fb6d8,#d7a98c)"><div class="label">Reaching Your Ideal Weight</div></div>
      <p>Learn how a healthy lifestyle enables you to lose weight, and keep the weight off without having to count calories.</p>
    </article>
    <article class="abs card" style="left:194px;top:792px">
      <div class="img" role="img" aria-label="Photo of an expecting couple embracing" style="background:linear-gradient(135deg,#e8e2dc,#b8968a)"><div class="label">Pregnancy and Baby Health</div></div>
      <p>Have an easy, fun, and healthy pregnancy; learn how pre, during, and post pregnancy affects your baby's health.</p>
    </article>
  </section>

  <aside>
    <h2 class="abs section-title" style="left:386px;top:597px">Health Networks</h2>
    <p class="abs networks-sub" style="left:386px;top:611px">The website consists of 10 health networks as follows</p>
    <ul class="abs net-list" style="left:386px;top:624px">
      <li><span class="net-ico"></span>Healthy Lifestyle</li>
      <li><span class="net-ico"></span>Health Problem</li>
      <li><span class="net-ico"></span>Weight Loss</li>
      <li><span class="net-ico" style="background:#5b8fc9"></span>Pregnancy</li>
      <li><span class="net-ico"></span>Female Health</li>
      <li><span class="net-ico"></span>Male Health</li>
      <li><span class="net-ico"></span>Child Health</li>
      <li><span class="net-ico"></span>Senior Health</li>
      <li><span class="net-ico"></span>Healthy Mind</li>
      <li><span class="net-ico"></span>Sports Nutrition</li>
    </ul>
    <div class="abs activity" style="left:382px">
      <div class="activity-head">Recent Activity<span class="sq"></span></div>
      <div class="act"><span class="ava"></span><div><b>Owen Harlow</b> liked <span class="ln">101 Conversion Tips To Help Improve Your Website</span> <i>· a few seconds ago</i></div></div>
      <div class="act"><span class="ava"></span><div><b>Tessa Marlin</b> liked <span class="ln">101 Conversion Tips To Help Improve Your Website</span> <i>· 7 minutes ago</i></div></div>
      <div class="act"><span class="ava"></span><div><b>Rosa Quill</b> liked <span class="ln">How to Ask Bloggers for Backlinks and Reviews</span> <i>· 20 hours ago</i></div></div>
      <div class="act"><span class="ava" style="background:#c8cdd8"></span><div><b>Social Media Growth Statistics</b><br><i>70 people shared this.</i></div></div>
    </div>
  </aside>

  <section class="abs signup">
    <div class="abs signup-btn">SIGNUP FREE TODAY</div>
    <p class="abs signup-text">And help and inspire others... Our site is not finished yet - but if you are keen to hear more, why not reserve your username below?<br>We'll send you and update when we're about to launch.</p>
    <div class="abs field" style="left:67px;width:173px">User Name</div>
    <div class="abs field" style="left:245px;width:173px">E Mail</div>
    <div class="abs go">SIGN UP</div>
  </section>

  <footer class="abs footer">
    <div class="abs follow">Follow Us</div>
    <div class="abs socials"><span></span><span></span><span></span></div>
    <nav class="abs foot-nav"><a>Home</a>| <a>About Us</a>| <a>Our Services</a>| <a>News</a>| <a>Blog</a>| <a>Contact Us</a></nav>
    <div class="abs copy">Copyrights @ 2014 All Rights Reserved</div>
  </footer>
</div>
</body>
</html>
```